WEBSITE NEEDED FOR MY COMPANY CALLED BRAVERIDGE HOCKEY DEVELOPMENT

LOOKING FOR A WEBSITE TO MARKET AND SEEL MY HOCKEY DEVELOPMENT PROGRAMS.
NEEDS TO HAVE 5+ PAGES

Target Market(s)

YOUTH SPORTS

Industry/Entity Type

YOUTH ATHLETE DEVELOPMENT

Number of Pages Required

5+ page

Font styles to use
Sans Serif

Colors
0054AA
0677BA
7BADD7
CADEEF
E8F1F8

Requirements
Must have
• MAIN PAGE - SPIRNG PROGRAM PAGE - SUMMER PROGRAM PAGE - WINTER PAGE - TOURNAMENT PAGE
Nice to have
• FLASH
Should not have
• NOT SURE

```html
<!DOCTYPE html>
<html lang="en">
<head>
<meta charset="utf-8">
<title>Braveridge Hockey Development</title>
<link href="https://fonts.googleapis.com/css2?family=Poppins:ital,wght@0,400;0,500;0,600;0,700;1,500;1,600;1,700&family=Lato:wght@400&display=swap" rel="stylesheet">
<style>
:root{
  --bg:#233242;
  --accent:#29b6e8;
  --white:#ffffff;
  --muted:#a9b3bd;
  --card-text:#8a8f96;
  --card-title:#2a3440;
  --line:#4a5867;
}
*{margin:0;padding:0;box-sizing:border-box}
html,body{width:1200px;height:2896px;overflow:hidden}
body{background:var(--bg);color:var(--white);font-family:'Poppins',sans-serif;position:relative}
.abs{position:absolute}
a{color:inherit;text-decoration:none}

.brand{left:86px;top:30px;width:260px;font-weight:700;font-size:24px;line-height:27px;color:var(--accent);letter-spacing:.5px}
.nav{right:86px;top:54px;display:flex;align-items:center;gap:0}
.nav a{font-size:15px;font-weight:500;padding:7px 13px;margin-left:6px;border-radius:6px}
.nav a.small{font-size:14px}
.nav a.active{background:var(--accent)}

.hero{left:86px;top:144px;width:1028px;height:596px;background:radial-gradient(ellipse at 35% 10%,#bfe6fb 0%,#5a7fa5 25%,#2a3b55 55%,#8e9aae 80%,#b9c1cd 100%)}
.hero-tag{position:absolute;left:61px;background:rgba(60,68,78,.85);font-weight:700;color:#fff;line-height:1}
.hero-tag.one{top:355px;height:65px;padding:0 24px;font-size:46px;display:flex;align-items:center}
.hero-tag.two{top:431px;height:64px;padding:0 24px;font-size:46px;display:flex;align-items:center}
.dots{position:absolute;left:62px;top:527px;display:flex;gap:8px}
.dots span{width:18px;height:18px;border-radius:3px;background:#c7cdd4}
.dots span.on{background:var(--accent)}

.program{top:796px;width:325px}
.program h2{font-size:28px;font-weight:600;line-height:34px}
.sub{font-size:14px;font-style:italic;font-weight:500;color:var(--accent)}
.program .photo{margin-top:18px;height:231px}
.program p{margin-top:24px;font-family:'Lato',sans-serif;font-size:13.5px;line-height:21px;color:var(--muted)}
.details{display:inline-flex;align-items:center;gap:8px;font-size:13px;font-weight:600;margin-top:24px}

.welcome{left:0;width:1200px;top:1298px;text-align:center}
.welcome h2{font-size:29px;font-weight:600;line-height:36px}
.player{left:100px;top:1384px;width:540px;height:551px;background:radial-gradient(ellipse at 45% 50%,#c9ced6 0%,#6f7a88 35%,rgba(35,50,66,0) 70%)}
.about{left:613px;top:1518px;width:440px}
.about h3{font-size:20px;font-weight:500;line-height:27px}
.about p{margin-top:20px;font-family:'Lato',sans-serif;font-size:13.5px;line-height:21px;color:var(--muted)}
.about p+p{margin-top:17px}
.btn{display:inline-block;margin-top:22px;background:var(--accent);border-radius:8px;width:132px;height:50px;line-height:50px;text-align:center;font-size:14px;font-weight:500}

.tour-head{left:86px;top:1998px}
.tour-head h2{font-size:29px;font-weight:600;line-height:36px}
.view-all{right:86px;top:2031px;display:flex;align-items:center;gap:10px;font-size:14px;font-weight:600}
.grid{left:86px;top:2079px;width:1028px;height:501px;display:grid;grid-template-columns:repeat(4,257px);grid-template-rows:250px 251px}
.cell-text{background:#fff;padding:30px 20px 0}
.date{font-size:13.5px;font-style:italic;font-weight:500;color:var(--accent)}
.cell-text h4{margin-top:8px;font-size:17px;line-height:21px;font-style:italic;font-weight:700;color:var(--card-title)}
.cell-text p{margin-top:16px;font-family:'Lato',sans-serif;font-size:13.5px;line-height:21px;color:var(--card-text)}
.cell-text .details{color:var(--accent);margin-top:8px;font-weight:500}

.foot-links{top:2666px;display:flex;gap:32px;font-size:15px}
.foot-brand{left:470px;top:2656px;width:260px;text-align:center;font-weight:700;font-size:22px;line-height:24px;color:var(--accent)}
.rule{left:86px;top:2737px;width:1028px;height:1px;background:var(--line)}
.copy{left:0;width:1200px;top:2762px;text-align:center;font-size:14.5px}
.social{top:2803px;width:40px;height:40px;border:1.5px solid #fff}
</style>
</head>
<body>

<header>
  <div class="abs brand">BRAVERIDGE<br>HOCKEY<br>DEVELOPMENT</div>
  <nav class="abs nav">
    <a class="active" href="#">HOME</a>
    <a href="#">SPIRNG PROGRAM</a>
    <a href="#">SUMMER PROGRAM</a>
    <a class="small" href="#">WINTER</a>
    <a class="small" href="#">TOURNAMENT</a>
  </nav>
</header>

<section class="abs hero" role="img" aria-label="Hockey players skating hard under arena lights">
  <div class="hero-tag one">BRAVERIDGE</div>
  <div class="hero-tag two">HOCKEY DEVELOPMENT</div>
  <div class="dots"><span class="on"></span><span></span><span></span></div>
</section>

<section>
  <article class="abs program" style="left:86px">
    <h2>SPIRNG PROGRAM</h2>
    <div class="sub">BRAVERIDGE HOCKEY DEVELOPMENT</div>
    <div class="photo" role="img" aria-label="Player shooting a puck with ice spray" style="background:linear-gradient(135deg,#2a4f78,#6d9cc6 50%,#1c2f48)"></div>
    <p>Pellentesque et tristique risus, sed tempor quam. Class aptent taciti sociosqu ad litora torquent per conubia nostra, per inceptos himenaeos. Vestibulum dapibus nulla quis lectus molestie egestas.</p>
    <a class="details" href="#">DETAILS <svg width="22" height="10" viewBox="0 0 22 10"><path d="M0 5H20M16 1L20 5L16 9" stroke="#fff" stroke-width="1.4" fill="none"/></svg></a>
  </article>
  <article class="abs program" style="left:437px">
    <h2>SUMMER PROGRAM</h2>
    <div class="sub">BRAVERIDGE HOCKEY DEVELOPMENT</div>
    <div class="photo" role="img" aria-label="Field hockey players on an outdoor pitch" style="background:linear-gradient(180deg,#3e4a2e,#8a8f5f 45%,#d6cfa8)"></div>
    <p>Pellentesque et tristique risus, sed tempor quam. Class aptent taciti sociosqu ad litora torquent per conubia nostra, per inceptos himenaeos. Vestibulum dapibus nulla quis lectus molestie egestas.</p>
    <a class="details" href="#">DETAILS <svg width="22" height="10" viewBox="0 0 22 10"><path d="M0 5H20M16 1L20 5L16 9" stroke="#fff" stroke-width="1.4" fill="none"/></svg></a>
  </article>
  <article class="abs program" style="left:788px">
    <h2>WINTER PROGRAM</h2>
    <div class="sub">BRAVERIDGE HOCKEY DEVELOPMENT</div>
    <div class="photo" role="img" aria-label="Players in red and white kits battling in front of goal" style="background:linear-gradient(135deg,#f2f4f7,#d94444 45%,#e9edf2)"></div>
    <p>Pellentesque et tristique risus, sed tempor quam. Class aptent taciti sociosqu ad litora torquent per conubia nostra, per inceptos himenaeos. Vestibulum dapibus nulla quis lectus molestie egestas.</p>
    <a class="details" href="#">DETAILS <svg width="22" height="10" viewBox="0 0 22 10"><path d="M0 5H20M16 1L20 5L16 9" stroke="#fff" stroke-width="1.4" fill="none"/></svg></a>
  </article>
</section>

<section>
  <div class="abs welcome">
    <h2>WELCOME TO OUR WEBSITE</h2>
    <div class="sub">BRAVERIDGE HOCKEY DEVELOPMENT</div>
  </div>
  <div class="abs player" role="img" aria-label="Hockey player skating forward with stick raised"></div>
  <div class="abs about">
    <h3>Lorem ipsum dolor sit amet, consectetur adipiscing elit.</h3>
    <p>Pellentesque et tristique risus, sed tempor quam. Class aptent taciti sociosqu ad litora torquent per conubia nostra, per inceptos himenaeos. Vestibulum dapibus nulla quis lectus molestie egestas. Fusce id metus quam. Pellentesque a odio et nisi convallis fermentum. Etiam eu risus eu urna vulputate sollicitudin. Fusce magna dui, vestibulum non suscipit nec, condimentum vitae diam. Suspendisse efficitur tempor dui.</p>
    <p>Pellentesque et tristique risus, sed tempor quam. Class aptent taciti sociosqu ad litora torquent per conubia nostra, per inceptos himenaeos. Vestibulum dapibus nulla quis lectus molestie egestas.</p>
    <a class="btn" href="#">LEARN MORE</a>
  </div>
</section>

<section>
  <div class="abs tour-head">
    <h2>OUR TOURNAMENT</h2>
    <div class="sub">BRAVERIDGE HOCKEY DEVELOPMENT</div>
  </div>
  <a class="abs view-all" href="#">VIEW ALL TOURNAMENTS <svg width="22" height="10" viewBox="0 0 22 10"><path d="M0 5H20M16 1L20 5L16 9" stroke="#fff" stroke-width="1.4" fill="none"/></svg></a>
  <div class="abs grid">
    <div role="img" aria-label="Skater driving toward the goalie" style="background:linear-gradient(135deg,#5d7c9e,#1c2636 55%,#9fb3c8)"></div>
    <div class="cell-text"><div class="date">12 AUGUST,2022</div><h4>LOREM IPSUM DOLOR SIT AMET, ADIPISCING ELIT.</h4><p>Pellentesque et tristique risus, sed tempor quam. Class aptent taciti sociosqu ad litora torquent per conubia nostra, per inceptos</p><a class="details" href="#">DETAILS <svg width="22" height="10" viewBox="0 0 22 10"><path d="M0 5H20M16 1L20 5L16 9" stroke="#29b6e8" stroke-width="1.4" fill="none"/></svg></a></div>
    <div role="img" aria-label="Youth floor hockey game in a gym" style="background:linear-gradient(180deg,#8c8a7c,#c9c3b3 50%,#e3ddd0)"></div>
    <div class="cell-text"><div class="date">12 AUGUST,2022</div><h4>LOREM IPSUM DOLOR SIT AMET, ADIPISCING ELIT.</h4><p>Pellentesque et tristique risus, sed tempor quam. Class aptent taciti sociosqu ad litora torquent per conubia nostra, per inceptos</p><a class="details" href="#">DETAILS <svg width="22" height="10" viewBox="0 0 22 10"><path d="M0 5H20M16 1L20 5L16 9" stroke="#29b6e8" stroke-width="1.4" fill="none"/></svg></a></div>
    <div class="cell-text"><div class="date">12 AUGUST,2022</div><h4>LOREM IPSUM DOLOR SIT AMET, ADIPISCING ELIT.</h4><p>Pellentesque et tristique risus, sed tempor quam. Class aptent taciti sociosqu ad litora torquent per conubia nostra, per inceptos</p><a class="details" href="#">DETAILS <svg width="22" height="10" viewBox="0 0 22 10"><path d="M0 5H20M16 1L20 5L16 9" stroke="#29b6e8" stroke-width="1.4" fill="none"/></svg></a></div>
    <div role="img" aria-label="Players racing for the puck on ice" style="background:linear-gradient(160deg,#4c6c8f,#1e2a3b 50%,#b7c6d6)"></div>
    <div class="cell-text"><div class="date">12 AUGUST,2022</div><h4>LOREM IPSUM DOLOR SIT AMET, ADIPISCING ELIT.</h4><p>Pellentesque et tristique risus, sed tempor quam. Class aptent taciti sociosqu ad litora torquent per conubia nostra, per inceptos</p><a class="details" href="#">DETAILS <svg width="22" height="10" viewBox="0 0 22 10"><path d="M0 5H20M16 1L20 5L16 9" stroke="#29b6e8" stroke-width="1.4" fill="none"/></svg></a></div>
    <div role="img" aria-label="Puck and sticks on ice in a lit arena" style="background:linear-gradient(180deg,#0f1a28,#3d6685 45%,#a9c1d4)"></div>
  </div>
</section>

<footer>
  <nav class="abs foot-links" style="left:87px"><a href="#">Home</a><a href="#">Spirng Program</a><a href="#">Summer Program</a></nav>
  <div class="abs foot-brand">BRAVERIDGE<br>HOCKEY DEVELOPMENT</div>
  <nav class="abs foot-links" style="right:86px"><a href="#">Winter</a><a href="#">Tournament</a><a href="#">Contact</a></nav>
  <div class="abs rule"></div>
  <div class="abs copy">©2022 Braveridge Hockey Development - Do not copy. All rights reserved.</div>
  <a class="abs social" style="left:524px" href="#" aria-label="Social profile one"></a>
  <a class="abs social" style="left:578px" href="#" aria-label="Social profile two"></a>
  <a class="abs social" style="left:632px" href="#" aria-label="Social profile three"></a>
</footer>

</body>
</html>
```